yourSmileCare Brookvale Business Card

Please design a two sided business card that is Elegant and Professional
Add subtle elegant patterns to suit Spot UV printing/ or raised printing

Name: Dr Marcus T. Fenwick
Qualification: BDSc (QLD)
Title: Dental Surgeon, Clinical Director
Company: yourSmileCare Brookvale
Phone: (02) 7593 2268
Address: Shop 7/18-20 Lindon Ave Brookvale 2097
email: info@yoursmilecarebrookvale.com.au
Facebook: facebook.com/yoursmilecarebrookvale

Motto:
Quality dentistry you can trust

Description of services (not compulsory):
Preventative Dentistry | General Dentistry
Cosmetic Dentistry | Teeth Whitening
Crown and Bridge | Root Canal Therapy
Veneers | Clearvono | Orthodontics
Emergency Dental Care | After Hours

Personalised Treatment Plans
Transparent Fees

Please make sure card is elegant and professional

Target Market(s)

general population, patients,
Dental sales companies, other professions

Industry/Entity Type

Dental Clinic

Contact Information for Business Card

Name: Dr Marcus T. Fenwick
Qualification: BDSc (QLD)
Phone: (02) 7593 2268
Address: Shop 7/18-20 Lindon Ave Brookvale

Motto:

Description of services (not compulsory)

Transparent Fees

Image of dental surgery optional

Please make sure card is elegant and profession

Requirements
Must have
• Logo
• Name, Title (next to name), Business
• Phone, address, facbeook
• Must have stylish design to suit SPOT UV reflective printing
Nice to have
• Subtle elegant patterns which will have Spot UV on them when printed
• Colours to match logo colour
• Description of services
Should not have
• Small fonts that are hard to read
• DO NOT PUT IMAGES OF DENTAL INSTRUMENTS OR TEETH PLEASE

```html
<!DOCTYPE html>
<html lang="en">
<head>
<meta charset="utf-8">
<title>yourSmileCare Brookvale Business Card</title>
<link rel="stylesheet" href="https://fonts.googleapis.com/css2?family=Arimo:wght@400;700&display=swap">
<style>
  :root {
    --backdrop: #000000;
    --card: #ffffff;
    --brand-green: #8dc63f;
    --brand-grey: #808285;
    --text-grey: #6d6e71;
  }
  * { margin: 0; padding: 0; box-sizing: border-box; }
  html, body {
    width: 999px; height: 1200px; overflow: hidden;
    background: var(--backdrop);
    font-family: "Arimo", Arial, sans-serif;
  }
  .stage { position: relative; width: 999px; height: 1200px; }
  .card {
    position: absolute; left: 62px; width: 875px; height: 497px;
    background: var(--card); border-radius: 42px; overflow: hidden;
  }
  .card--front { top: 92px; }
  .card--back { top: 625px; }

  .front-band { position: absolute; left: 0; bottom: 0; width: 875px; height: 90px; }

  .wordmark {
    position: absolute; color: var(--brand-green); font-weight: 700;
    text-align: center; line-height: 1.05; letter-spacing: -0.5px;
  }
  .wordmark__dot {
    display: block; margin: 0 auto; border-radius: 50%; background: var(--brand-green);
  }
  .card--front .wordmark { left: 52px; top: 172px; width: 300px; font-size: 38px; }
  .card--front .wordmark__dot { width: 22px; height: 22px; margin-bottom: 14px; }
  .card--back .wordmark { left: 0; top: 130px; width: 875px; font-size: 68px; }
  .card--back .wordmark__dot { width: 34px; height: 34px; margin-bottom: 22px; }

  .details { position: absolute; left: 481px; top: 96px; color: var(--text-grey); font-size: 20.5px; line-height: 30px; }
  .details__name { color: var(--brand-green); font-size: 38px; font-weight: 700; line-height: 44px; margin-bottom: 12px; }
  .details__address { margin-top: 31px; }
  .details__contact { margin-top: 17px; line-height: 29px; }
</style>
</head>
<body>
<main class="stage">
  <section class="card card--front">
    <div class="wordmark"><span class="wordmark__dot"></span>yourSmileCare<br>Brookvale</div>
    <div class="details">
      <p class="details__name">Dr Marcus T. Fenwick</p>
      <p>BDSc (QLD)</p>
      <p>Dental Surgeon, Clinical Director</p>
      <p class="details__address">Shop 7/18-20 Lindon Ave<br>Brookvale</p>
      <p class="details__contact">(02) 7593 2268<br>info@yoursmilecarebrookvale.com.au<br>facebook.com/yoursmilecarebrookvale</p>
    </div>
    <svg class="front-band" viewBox="0 0 875 90" aria-hidden="true">
      <path d="M0 17 H340 C365 17 375 30 392 43 H875 V90 H0 Z" fill="var(--brand-green)"/>
      <path d="M383 37 C395 48 405 53 425 53 H875 V43 H392 C389 41 386 39 383 37 Z" fill="var(--brand-green)"/>
      <path d="M382 36 C400 50 410 59 430 59 H875 V42 H394 Z" fill="var(--brand-grey)"/>
    </svg>
  </section>

  <section class="card card--back">
    <div class="wordmark"><span class="wordmark__dot"></span>yourSmileCare<br>Brookvale</div>
  </section>
</main>
</body>
</html>
```